Used Truck and Machinery dealer needs a new website

We require a new website four our business which is in the early stages of becoming fully online. We have been a truck and machinery dealer in Western Australia since 1974. We have had many tries at websites over the years, but have never been too pleased with the result (mainly because I have tried doing it myself, rather than a professional). Currently, we run an Pagelofty site as a stop gap (seen at www.haulerandrig.com.au) which a super awesome design company threw together for us, but we need to iframe (shudder) our stock into the page from a third party inventory site (This will change most likely to the motorbin dealer network in the near future, which uses a script to integrate) (Direct link to the stock on the current site: https://www.rigmarket.com.au/search/hauler-(and)-rig/all-for-sale/?query=v~1-z~15-) I want the page to be responsive (knowing full well having an iframe makes this difficult, so interested to see what can be done there), Most of the clientele prefer to phone, so having a layout similar to what you can see on our Ppagelofty works (i.e. our number to be seen as soon as you are on page), also have a request callback feature (e.g. contact form). We also need a second contact form to be added for Valuations. In a nutshell, we value all types of vehicles, including trailers and machines to ensure that the client is paying the correct insurance premium, plus we value equipment for 99% of Australia's insurance companies when a dispute is made regarding the true value of the item. I would like a google map embedded to find our premises. I want the site to be SEO'd. I like the current design but would like it to be more colour neutral, but tying in with our company logo. Ideally, I want to use a popular CMS such as Wordpress or Drupal but open to others if you feel there is a better option.
I have mentioned 3 pages, on the main page is to have about us with the following text:
"Corrabee Hauler and Rig have been a specialist in heavy trucks and machinery for over 35 years. We source equipment on request, consign vehicles and have a steady flow of new stock arriving weekly.

We have been operating as a licensed valuer for vehicles large and small for a number of years and are contracted to 99% of Australia’s insurance companies to value pre accident vehicles.

We also conduct full fleet valuations to help you keep your premiums at a realistic figure."

It should have our contact details, plus our address.

The second page should have our stock listed and integrated with https://www.rigmarket.com.au/search/hauler-(and)-rig/all-for-sale/?query=v~1-z~15-

The Third page should be a contact page with the usual contact form but also have an evaluation form also with the following fields:
Name, Email, Phone, Location of Item(s), Make, Model, Year, Registration Number, Condition (Drop down with Excellent | Fair | Poor) and, Additional Comments

It should have social icons to Facebook and Instagram:
Facebook Link: http://facebook.com/corrabeehaulers
Instagram Link: https://www.instagram.com/haulerandrigcorrabee/

I have uploaded some of our artwork to assist.Finally, we have our own hosting with HostNubo which includes:15GB High-Speed SSD Storage Unlimited Premium Bandwidth Unlimited Addon & Parked Domains Unlimited MariaDB Databases 200% CPU Allowance 4GB Memory Allowance Hourly Varkelo Backups FREE Tessime SSL Certificates I will give the winning designer access to the hosting platform to upload the final design and have it live at www.haulerandrig.com.auI will require an overview of the site on how to maintain moving forward. Thank you

Target Market(s)

People wishing to purchase a used heavy vehicle such as a Truck, Trailer or Machine

Industry/Entity Type

Automotive

Coding

Coded - Design and coding required

Number of Pages Required

3 page

Font styles to use
Serif
Sans Serif
Decorative
Script

Colors

Designer to choose colors to be used in the design.

Requirements
Must have
• Integration into the existing stock located at https://www.rigmarket.com.au/search/hauler-(and)-rig/all-for-sale/?query=v~1-z~15-)
• Must be on our hosting platform at HostNubo
• Must be as responsive as possible even though you will have to integrate with a third party site
• Must be on a popular CMS
• Must be SEO'd

```html
<!DOCTYPE html>
<html lang="en">
<head>
<meta charset="utf-8">
<title>Hauler&amp;Rig — Get an Evaluation</title>
<link href="https://fonts.googleapis.com/css2?family=Poppins:wght@300;400;600;700&family=Questrial&family=Open+Sans:wght@400&family=Archivo:wght@700;800&display=swap" rel="stylesheet">
<style>
  :root {
    --red: #e8132b;
    --white: #ffffff;
    --ink: #1d1d1d;
    --muted: #7a7a7a;
    --panel: #f1f1f1;
    --field-border: #e3e3e3;
    --hero-dark: #2a1810;
    --hero-mid: #5a3220;
    --hero-warm: #7a4326;
  }
  * { box-sizing: border-box; margin: 0; padding: 0; }
  html, body { width: 1048px; height: 1200px; overflow: hidden; background: var(--white); }
  .page { position: relative; width: 1048px; height: 1200px; font-family: "Poppins", sans-serif; color: var(--ink); }

  .hero { position: absolute; left: 0; top: 0; width: 1048px; height: 415px; overflow: hidden; }
  .hero-photo {
    position: absolute; inset: 0;
    background:
      radial-gradient(ellipse at 78% 85%, rgba(150,80,40,0.55), transparent 55%),
      radial-gradient(ellipse at 20% 20%, rgba(110,95,80,0.45), transparent 50%),
      linear-gradient(180deg, var(--hero-mid) 0%, var(--hero-dark) 45%, var(--hero-warm) 100%);
  }
  .brand { position: absolute; left: 0; right: 0; top: 74px; display: flex; justify-content: center; align-items: center; gap: 10px; }
  .brand-mark { width: 22px; height: 22px; background: var(--red); }
  .brand-name { font-family: "Archivo", sans-serif; font-weight: 800; font-size: 26px; color: var(--white); letter-spacing: -0.5px; }
  .hero-title { position: absolute; left: 0; right: 0; top: 204px; text-align: center; font-family: "Archivo", sans-serif; font-weight: 700; font-size: 40px; color: var(--white); letter-spacing: 0.5px; }
  .pill { display: flex; align-items: center; justify-content: center; background: var(--red); color: var(--white); font-family: "Poppins", sans-serif; font-weight: 600; border-radius: 30px; }
  .hero-cta { position: absolute; left: 425px; top: 272px; width: 198px; height: 49px; font-size: 15px; }

  .intro { position: absolute; left: 110px; top: 457px; width: 828px; text-align: center; font-family: "Questrial", sans-serif; font-size: 15px; line-height: 29px; color: var(--ink); }

  .evaluation { position: absolute; left: 0; top: 582px; width: 1048px; height: 552px; background: var(--panel); }
  .evaluation-title { position: absolute; left: 0; right: 0; top: 64px; text-align: center; font-weight: 600; font-size: 30px; color: var(--red); letter-spacing: -0.2px; }
  .field { position: absolute; background: var(--white); border: 1px solid var(--field-border); box-shadow: inset 0 2px 3px rgba(0,0,0,0.07); font-family: "Open Sans", sans-serif; font-size: 10.5px; color: #333; padding: 0 14px; display: flex; align-items: center; }
  .field.col-left { left: 157px; width: 358px; height: 35px; }
  .field.col-right { left: 531px; width: 359px; height: 35px; }
  .field.message { left: 531px; width: 359px; top: 234px; height: 126px; align-items: flex-start; padding-top: 10px; }

  .captcha { position: absolute; left: 432px; top: 373px; width: 184px; height: 51px; background: #f9f9f9; border: 1px solid #dcdcdc; box-shadow: 0 1px 2px rgba(0,0,0,0.08); font-family: "Open Sans", sans-serif; }
  .captcha-box { position: absolute; left: 12px; top: 16px; width: 18px; height: 18px; border: 2px solid #c1c1c1; background: var(--white); border-radius: 2px; }
  .captcha-label { position: absolute; left: 37px; top: 17px; font-size: 10.5px; color: #222; }
  .captcha-seal { position: absolute; left: 138px; top: 8px; width: 22px; height: 22px; border-radius: 50%; background: #9aa4b8; }
  .captcha-name { position: absolute; left: 126px; top: 34px; width: 50px; text-align: center; font-size: 7.5px; color: #777; }

  .upload { position: absolute; left: 368px; top: 440px; width: 148px; height: 42px; font-size: 14.5px; gap: 7px; }
  .submit { position: absolute; left: 532px; top: 440px; width: 148px; height: 42px; font-size: 14.5px; }

  .footer { position: absolute; left: 0; right: 0; top: 1154px; text-align: center; font-weight: 300; font-size: 15px; color: var(--muted); }
</style>
</head>
<body>
<div class="page">
  <header class="hero">
    <div class="hero-photo" role="img" aria-label="Photograph of an outback dirt track through dry bushland with an old truck wreck, in dark reddish-brown tones"></div>
    <div class="brand">
      <span class="brand-mark"></span>
      <span class="brand-name">HAULER&amp;RIG</span>
    </div>
    <h1 class="hero-title">GET AN EVALUATION</h1>
    <div class="pill hero-cta">REQUEST CALL BACK</div>
  </header>

  <p class="intro">At vero eos et accusamus et iusto odio dignissimos ducimus qui blanditiis praesentium voluptatum deleniti atque corrupti quos dolores et quas molestias excepturi sint occaecati cupiditate non provident, similique sunt in culpa qui officia deserunt mollitia animi, id est laborum et dolorum fuga</p>

  <section class="evaluation">
    <h2 class="evaluation-title">GET AN EVALUATION FROM&nbsp; PERTH'S TRUCK EXPERTS</h2>

    <div class="field col-left" style="top:140px">Name</div>
    <div class="field col-right" style="top:140px">Email</div>
    <div class="field col-left" style="top:186px">Phone Number</div>
    <div class="field col-right" style="top:186px">Suburb of Item</div>
    <div class="field col-left" style="top:234px">Make</div>
    <div class="field message">Message :</div>
    <div class="field col-left" style="top:279px">Model</div>
    <div class="field col-left" style="top:324px">Registration</div>

    <div class="captcha">
      <span class="captcha-box"></span>
      <span class="captcha-label">I'm not a robot</span>
      <span class="captcha-seal"></span>
      <span class="captcha-name">Verifly</span>
    </div>

    <div class="pill upload">
      <svg width="13" height="13" viewBox="0 0 13 13" aria-hidden="true"><path d="M6.5 1v11M1 6.5h11" stroke="#fff" stroke-width="2.6" stroke-linecap="round"/></svg>
      UPLOAD FILES
    </div>
    <div class="pill submit">SUBMIT NOW</div>
  </section>

  <footer class="footer">© 2018 Company Name&nbsp; All right reserved&nbsp; Term of Use</footer>
</div>
</body>
</html>
```